Bright Path Therapies business cards and stationary

Need business cards and stationary designed to match previously made logo for for a new company based in Sydney NSW called 'Bright Path Therapies'.

We provide early intervention services and diagnostic assessment for children with disability and their families. I would like designs that are colourful and child friendly - possibly using feet/footprints/steps on a white background. The final design should communicate that we are family friendly, accepting and fun to work with.

Target Market(s)

Parents and Families
Teachers
Allied Health Professionals

Industry/Entity Type

Psychology

Contact Information for Business Card

Bright Path Therapies
www.brightpaththerapies.example
info@brightpaththerapies.example

Font styles to use
Sans Serif
Decorative
Script

Requirements
Must have
• Match the font and colour scheme of logo, along with footprint picture
Nice to have
• Clean and simple, while reflecting that I am working with families.
• Also- editable for when we make staff specific cards.

```html
<!DOCTYPE html>
<html lang="en">
<head>
<meta charset="utf-8">
<title>Bright Path Therapies – Business Cards</title>
<link rel="stylesheet" href="https://fonts.googleapis.com/css2?family=Amatic+SC:wght@700&family=Quicksand:wght@500;600&display=swap">
<style>
  :root {
    --page-bg: #2b2b2b;
    --card-white: #ffffff;
    --pattern-grey: #eeeeee;
    --brand-blue: #1f6fb8;
    --band-blue: #2272bd;
    --band-blue-light: #2a82cc;
    --brand-red: #e8432f;
    --text-grey: #6b6b6b;
  }
  * { margin: 0; padding: 0; box-sizing: border-box; }
  html, body {
    width: 1200px; height: 900px; overflow: hidden;
    background: var(--page-bg);
    font-family: "Quicksand", sans-serif;
  }
  .canvas { position: relative; width: 1200px; height: 900px; }

  .card {
    position: absolute;
    width: 560px; height: 320px;
    border-radius: 26px;
    background: var(--card-white);
    overflow: hidden;
    box-shadow: 0 14px 30px rgba(0,0,0,.45);
  }
  .card--front { left: 70px; top: 110px; }
  .card--back  { left: 570px; top: 470px; }

  .footprint-pattern {
    position: absolute; inset: 0;
    background: radial-gradient(circle at 50% 50%, var(--card-white) 0%, var(--pattern-grey) 85%);
  }

  .brand {
    position: absolute;
    display: flex; align-items: center; gap: 12px;
  }
  .brand__mark {
    width: 54px; height: 54px; border-radius: 50%;
    background: var(--brand-red); flex: none;
  }
  .brand__name {
    font-family: "Quicksand", sans-serif;
    font-weight: 600;
    font-size: 30px;
    line-height: 1;
    color: var(--brand-blue);
    white-space: nowrap;
  }
  .card--front .brand { left: 50%; top: 50%; transform: translate(-50%, -50%); }
  .card--back .brand { right: 34px; top: 38px; }
  .card--back .brand__mark { width: 44px; height: 44px; }
  .card--back .brand__name { font-size: 24px; }

  .back-band { position: absolute; inset: 0; }

  .person { position: absolute; left: 34px; top: 112px; }
  .person__name {
    font-family: "Amatic SC", sans-serif;
    font-weight: 700;
    font-size: 34px;
    letter-spacing: 1px;
    color: var(--brand-red);
    line-height: 1;
  }
  .person__role {
    font-size: 15px; font-weight: 500;
    color: var(--text-grey);
    margin-top: 2px;
  }

  .contact {
    position: absolute; left: 40px; top: 226px;
    list-style: none;
    color: var(--card-white);
    font-size: 14px; font-weight: 500;
  }
  .contact__item { display: flex; align-items: center; gap: 10px; height: 24px; white-space: nowrap; }
  .contact__icon { width: 14px; height: 14px; flex: none; }
</style>
</head>
<body>
<main class="canvas">

  <section class="card card--front">
    <div class="footprint-pattern" role="img" aria-label="Faint scattered grey footprint pattern"></div>
    <div class="brand">
      <span class="brand__mark"></span>
      <span class="brand__name">Bright Path Therapies</span>
    </div>
  </section>

  <section class="card card--back">
    <svg class="back-band" width="560" height="320" viewBox="0 0 560 320" aria-hidden="true">
      <defs>
        <linearGradient id="bandGradient" x1="0" y1="1" x2="1" y2="0">
          <stop offset="0" stop-color="#2272bd"/>
          <stop offset="1" stop-color="#2a82cc"/>
        </linearGradient>
      </defs>
      <polygon points="0,200 460,104 530,104 470,306 0,306" fill="url(#bandGradient)"/>
      <circle cx="490" cy="136" r="50" fill="#e8432f"/>
    </svg>

    <div class="brand">
      <span class="brand__mark"></span>
      <span class="brand__name">Bright Path Therapies</span>
    </div>

    <div class="person">
      <p class="person__name">Morgan L. Hartley</p>
      <p class="person__role">Founder</p>
    </div>

    <ul class="contact">
      <li class="contact__item">
        <svg class="contact__icon" viewBox="0 0 14 14" aria-hidden="true"><rect x="3.5" y="1" width="7" height="12" rx="1.5" fill="none" stroke="#fff" stroke-width="1.3"/><circle cx="7" cy="11" r=".8" fill="#fff"/></svg>
        <span>555-014-2671</span>
      </li>
      <li class="contact__item">
        <svg class="contact__icon" viewBox="0 0 14 14" aria-hidden="true"><rect x="1" y="3" width="12" height="8" fill="none" stroke="#fff" stroke-width="1.3"/><path d="M1 3 L7 8 L13 3" fill="none" stroke="#fff" stroke-width="1.3"/></svg>
        <span>info@brightpaththerapies.example</span>
      </li>
      <li class="contact__item">
        <svg class="contact__icon" viewBox="0 0 14 14" aria-hidden="true"><circle cx="7" cy="7" r="5.8" fill="none" stroke="#fff" stroke-width="1.2"/><ellipse cx="7" cy="7" rx="2.6" ry="5.8" fill="none" stroke="#fff" stroke-width="1"/><path d="M1.2 7 H12.8" stroke="#fff" stroke-width="1"/></svg>
        <span>www.brightpaththerapies.example</span>
      </li>
    </ul>
  </section>

</main>
</body>
</html>
```